Business Card for IT company

I need a high tech looking business card using our logo. I prefer something clean and modern.

Target Market(s)

Buyers of IT hardware and software, IT Techies who are key influencers

Industry/Entity Type

Business

```html
<!DOCTYPE html>
<html lang="en">
<head>
<meta charset="utf-8">
<title>ZEVK Consulting — Business Card</title>
<link rel="stylesheet" href="https://fonts.googleapis.com/css2?family=Montserrat:wght@400;600&family=Questrial&display=swap">
<style>
  :root {
    --card-bg: #e9efec;
    --ink-dark: #232829;
    --accent-green: #4fd61a;
    --gear-light: #c9d3d1;
    --gear-mid: #a7aeae;
    --gear-dark: #5f6364;
    --hex-tint: #d6ebcf;
    --divider: #c4cbc9;
  }
  html, body {
    margin: 0;
    padding: 0;
    width: 1200px;
    height: 720px;
    overflow: hidden;
    background: var(--card-bg);
  }
  .card {
    position: relative;
    width: 1200px;
    height: 720px;
    overflow: hidden;
    background: var(--card-bg);
  }
  .deco {
    position: absolute;
    border-radius: 50%;
  }
  .deco--large-gear {
    left: -260px;
    top: -210px;
    width: 820px;
    height: 820px;
    background: radial-gradient(circle, rgba(201,211,209,0) 0 55%, var(--gear-light) 56% 100%);
  }
  .deco--gear-top {
    left: -10px;
    top: -32px;
    width: 150px;
    height: 150px;
    background: radial-gradient(circle, rgba(0,0,0,0) 0 55%, var(--gear-mid) 56% 100%);
  }
  .deco--gear-mid {
    left: 62px;
    top: 92px;
    width: 148px;
    height: 148px;
    background: radial-gradient(circle, rgba(0,0,0,0) 0 57%, var(--gear-dark) 58% 100%);
  }
  .deco--gear-corner {
    left: 1014px;
    top: 534px;
    width: 146px;
    height: 146px;
    background: radial-gradient(circle, rgba(0,0,0,0) 0 30%, var(--gear-light) 31% 100%);
  }
  .deco--hex-field {
    left: 620px;
    top: 160px;
    width: 580px;
    height: 560px;
    border-radius: 0;
    background: radial-gradient(ellipse at 60% 50%, var(--hex-tint) 0%, rgba(214,235,207,0.35) 45%, rgba(233,239,236,0) 72%);
  }
  .divider {
    position: absolute;
    left: 236px;
    top: 160px;
    height: 490px;
    border-left: 2px dashed var(--divider);
  }
  .brand {
    position: absolute;
    left: 371px;
    top: 0;
    width: 762px;
    height: 380px;
    margin: 0;
  }
  .brand svg {
    display: block;
    width: 762px;
    height: 380px;
    overflow: visible;
  }
  .brand__word {
    font-family: "Montserrat", sans-serif;
    font-weight: 600;
    font-size: 282px;
    fill: var(--ink-dark);
  }
  .brand__tag {
    font-family: "Montserrat", sans-serif;
    font-weight: 400;
    font-size: 66px;
    fill: var(--ink-dark);
  }
  .contact {
    position: absolute;
    left: 0;
    top: 482px;
    margin: 0;
    font-family: "Questrial", sans-serif;
    font-variant: small-caps;
  }
  .contact__row {
    display: flex;
    align-items: baseline;
    margin: 0;
  }
  .contact__label {
    width: 224px;
    text-align: right;
    color: var(--ink-dark);
    font-size: 34px;
    line-height: 35px;
  }
  .contact__value {
    margin-left: 25px;
    color: var(--accent-green);
    font-size: 34px;
    line-height: 35px;
  }
  .contact__row--name .contact__label,
  .contact__row--name .contact__value {
    font-size: 60px;
    line-height: 58px;
  }
</style>
</head>
<body>
  <main class="card">
    <div class="deco deco--large-gear" role="img" aria-label="Large faint grey gear decoration"></div>
    <div class="deco deco--hex-field" role="img" aria-label="Faint green hexagon grid pattern"></div>
    <div class="deco deco--gear-top" role="img" aria-label="Small grey gear decoration"></div>
    <div class="deco deco--gear-mid" role="img" aria-label="Small dark grey gear decoration"></div>
    <div class="deco deco--gear-corner" role="img" aria-label="Double light grey gear decoration"></div>

    <div class="divider"></div>

    <h1 class="brand">
      <svg viewBox="0 0 762 380" aria-label="ZEVK Consulting">
        <text class="brand__word" x="0" y="269" textLength="760" lengthAdjust="spacingAndGlyphs">ZEVK</text>
        <text class="brand__tag" x="2" y="352" textLength="758" lengthAdjust="spacing">CONSULTING</text>
      </svg>
    </h1>

    <dl class="contact">
      <div class="contact__row contact__row--name">
        <dt class="contact__label">Name</dt>
        <dd class="contact__value">Ellis Marren</dd>
      </div>
      <div class="contact__row">
        <dt class="contact__label">Title</dt>
        <dd class="contact__value">Operation Manager</dd>
      </div>
      <div class="contact__row">
        <dt class="contact__label">Phone</dt>
        <dd class="contact__value">1-555-014729</dd>
      </div>
      <div class="contact__row">
        <dt class="contact__label">Email</dt>
        <dd class="contact__value">ellis@zevk.example</dd>
      </div>
    </dl>
  </main>
</body>
</html>
```